Natural Immune System Booster

We need a pharmaceutical type box and label design for a vitamin supplement product. Pravolex is in process of being trademarked and should therefore carry the TM symbol. It is comprised of a special blend of over 20 vitamins, herbs and minerals with a High strength vitamin C booster. The tag line should read. The No.1 Natural Support For Your Immune System. Each tube contains 10 tablets. A bar code will be placed on the box carton. We prefer bright and vivid colours, preferably a mix of electric purple, yellow and orange mix. We have three flavours, summer berry (strawberry), tropical fruit and juicy orange - the box and label should indicate the flavours in a creative design element. Effervescent tabelts should be clearly marked on the box and label. The ingredients and instructions should be present on the box outer carton and also the label. We require an eye catching yet simple and bright design that pops off the shelf.
Updates

Target Market(s)

Target customers are male and female 20 - 60+ that live in Western countries that handle household budgets.

Industry/Entity Type

Pharmaceutical

Requirements
Must have
• Please see current box design, all necessary elements and specifications are included here. We require same to be placed on new design.

I have attached a txt file of the supplement facts and other details that are required for both the label and the box

```html
<!DOCTYPE html>
<html lang="en">
<head>
<meta charset="utf-8">
<title>Pravolex Packaging – Idea One</title>
<link rel="stylesheet" href="https://fonts.googleapis.com/css2?family=Alfa+Slab+One&family=Audiowide&family=Lato:wght@300;400&display=swap">
<style>
  :root {
    --paper: #ffffff;
    --ink: #1a1a1a;
    --green: #138a43;
    --white: #ffffff;
  }
  html, body {
    margin: 0;
    padding: 0;
    width: 1200px;
    height: 927px;
    overflow: hidden;
    background: var(--paper);
  }
  .sheet {
    position: relative;
    width: 1200px;
    height: 927px;
  }
  .sheet-title {
    position: absolute;
    left: 30px;
    top: 26px;
    margin: 0;
    font: 300 23px/1 "Lato", sans-serif;
    color: var(--ink);
  }
  .sheet-subtitle {
    position: absolute;
    left: 0;
    width: 1200px;
    top: 80px;
    margin: 0;
    text-align: center;
    font: 300 23px/1 "Lato", sans-serif;
    color: var(--ink);
  }
  .pack {
    position: absolute;
    width: 451px;
    height: 166px;
    border: 1.5px solid var(--ink);
    box-shadow: 0 10px 26px rgba(0,0,0,0.08);
    overflow: hidden;
  }
  .pack svg { display: block; width: 100%; height: 100%; }

  .pack--berry {
    left: 216px; top: 211px;
    --bg: #e8202a; --stripe-dark: #8e1a1f; --stripe-a: #f7a21b;
    --stripe-b: #8e1a1f; --stripe-c: #f7a21b; --splash: #9b1b22;
    --badge: #e8202a;
  }
  .pack--tropical {
    left: 388px; top: 404px;
    --bg: #ffe000; --stripe-dark: #e8452a; --stripe-a: #f39a1e;
    --stripe-b: #e8452a; --stripe-c: #f7a21b; --splash: #f0a21c;
    --badge: #f5d100;
  }
  .pack--orange {
    left: 560px; top: 598px;
    --bg: #ee7124; --stripe-dark: #e0452a; --stripe-a: #f39a1e;
    --stripe-b: #e0452a; --stripe-c: #f39a1e; --splash: #e8452a;
    --badge: #e8452a;
  }

  .pack-bg { fill: var(--bg); }
  .stripe-dark { fill: var(--stripe-dark); }
  .stripe-green { fill: var(--green); }
  .stripe-a { fill: var(--stripe-a); }
  .stripe-b { fill: var(--stripe-b); }
  .stripe-c { fill: var(--stripe-c); }
  .flavour-splash { fill: var(--splash); }
  .count-badge { fill: var(--badge); stroke: var(--white); stroke-width: 1; }
  .count-number { font: 400 13px "Audiowide", sans-serif; fill: var(--white); }
  .count-unit { font: 400 4.5px "Lato", sans-serif; fill: var(--white); }
  .brand-name { font: 400 21px "Alfa Slab One", serif; fill: var(--white); }
  .tagline-main { font: 400 9.5px "Audiowide", sans-serif; fill: var(--white); }
  .tagline-sub { font: 400 5px "Lato", sans-serif; fill: var(--white); }
  .flavour-name { font: 400 14px "Alfa Slab One", serif; fill: var(--white); }
</style>
</head>
<body>
<main class="sheet">
  <h1 class="sheet-title">Pravolex Packaging</h1>
  <h2 class="sheet-subtitle">IDEA ONE - packaging for three flavour</h2>

  <section class="pack pack--berry" aria-label="Pravolex Summer Berry box">
    <svg viewBox="0 0 412 152" preserveAspectRatio="none">
      <rect class="pack-bg" width="412" height="152"/>
      <polygon class="stripe-dark" points="0,58 412,-27 412,-19 0,66"/>
      <polygon class="stripe-green" points="0,70 412,-15 412,43 0,128"/>
      <polygon class="stripe-a" points="0,132 412,47 412,57 0,142"/>
      <polygon class="stripe-b" points="0,146 412,61 412,75 0,160"/>
      <polygon class="stripe-c" points="0,164 412,79 412,95 0,180"/>
      <path class="flavour-splash" role="img" aria-label="Berry juice splash" d="M250,70 Q290,45 335,62 Q370,80 355,118 Q340,150 290,146 Q245,140 240,108 Q236,84 250,70Z"/>
      <text class="brand-name" x="62" y="78">Pravolex™</text>
      <g transform="rotate(-11.66 0 0)">
        <text class="tagline-main" x="250" y="89">The No.1 Natural</text>
        <text class="tagline-sub" x="250" y="97">Support For Your Immune System</text>
      </g>
      <g transform="rotate(-10 295 100)">
        <text class="flavour-name" x="295" y="97" text-anchor="middle">SUMMER</text>
        <text class="flavour-name" x="295" y="113" text-anchor="middle">BERRY</text>
      </g>
      <circle class="count-badge" cx="34" cy="107" r="17"/>
      <text class="count-number" x="34" y="108" text-anchor="middle">10</text>
      <text class="count-unit" x="34" y="115" text-anchor="middle">tablets</text>
    </svg>
  </section>

  <section class="pack pack--tropical" aria-label="Pravolex Tropical Fruit box">
    <svg viewBox="0 0 412 152" preserveAspectRatio="none">
      <rect class="pack-bg" width="412" height="152"/>
      <polygon class="stripe-dark" points="0,58 412,-27 412,-19 0,66"/>
      <polygon class="stripe-green" points="0,70 412,-15 412,43 0,128"/>
      <polygon class="stripe-a" points="0,132 412,47 412,57 0,142"/>
      <polygon class="stripe-b" points="0,146 412,61 412,75 0,160"/>
      <polygon class="stripe-c" points="0,164 412,79 412,95 0,180"/>
      <path class="flavour-splash" role="img" aria-label="Tropical juice splash" d="M250,70 Q290,45 335,62 Q370,80 355,118 Q340,150 290,146 Q245,140 240,108 Q236,84 250,70Z"/>
      <text class="brand-name" x="62" y="78">Pravolex™</text>
      <g transform="rotate(-11.66 0 0)">
        <text class="tagline-main" x="250" y="89">The No.1 Natural</text>
        <text class="tagline-sub" x="250" y="97">Support For Your Immune System</text>
      </g>
      <g transform="rotate(-10 295 100)">
        <text class="flavour-name" x="295" y="97" text-anchor="middle">TROPICAL</text>
        <text class="flavour-name" x="295" y="113" text-anchor="middle">FRUIT</text>
      </g>
      <circle class="count-badge" cx="34" cy="107" r="17"/>
      <text class="count-number" x="34" y="108" text-anchor="middle">10</text>
      <text class="count-unit" x="34" y="115" text-anchor="middle">tablets</text>
    </svg>
  </section>

  <section class="pack pack--orange" aria-label="Pravolex Juicy Orange box">
    <svg viewBox="0 0 412 152" preserveAspectRatio="none">
      <rect class="pack-bg" width="412" height="152"/>
      <polygon class="stripe-dark" points="0,58 412,-27 412,-19 0,66"/>
      <polygon class="stripe-green" points="0,70 412,-15 412,43 0,128"/>
      <polygon class="stripe-a" points="0,132 412,47 412,57 0,142"/>
      <polygon class="stripe-b" points="0,146 412,61 412,75 0,160"/>
      <polygon class="stripe-c" points="0,164 412,79 412,95 0,180"/>
      <path class="flavour-splash" role="img" aria-label="Orange juice splash" d="M250,70 Q290,45 335,62 Q370,80 355,118 Q340,150 290,146 Q245,140 240,108 Q236,84 250,70Z"/>
      <text class="brand-name" x="62" y="78">Pravolex™</text>
      <g transform="rotate(-11.66 0 0)">
        <text class="tagline-main" x="250" y="89">The No.1 Natural</text>
        <text class="tagline-sub" x="250" y="97">Support For Your Immune System</text>
      </g>
      <g transform="rotate(-10 295 100)">
        <text class="flavour-name" x="295" y="97" text-anchor="middle">JUICY</text>
        <text class="flavour-name" x="295" y="113" text-anchor="middle">ORANGE</text>
      </g>
      <circle class="count-badge" cx="34" cy="107" r="17"/>
      <text class="count-number" x="34" y="108" text-anchor="middle">10</text>
      <text class="count-unit" x="34" y="115" text-anchor="middle">tablets</text>
    </svg>
  </section>
</main>
</body>
</html>
```